Wix site for a family history research service / genealogist

Design a Wix website for a genealogy/family history research business.

The colour scheme and logo exist and the main imagery has been selected and purchased. The main emotion I'd like the website to convey is "looking up" - like looking up your family tree, looking up a DNA helix, looking up to your parents, grandparents etc. I want the vibe to be one that is enthusiastic about the potential discoveries in your family's history you can make on my website. My service is to the general public, but the main target group are older people 50+ in Australia (I advertise in retirement homes, on golf courses etc.).
I'd like the website to be
- friendly, warm, approachable, trustworthy and open in terms of it's feel
- easy to read, understand and navigate for older people (this is important)
- feature a "language switch" that allows for 3 languages. Ideally pre-selected by geographic origin of visitor.
- Show clear pathways to action (contact or purchase)
- Has a simply shopping cart function that connects to PayPal

The website sections are as follows:
1. A general "Home" page or section
2. About us/me
3. Services (there will be an initial 4 products/services)
3.1 Traditional genealogy (2 products)
3.2 DNA-based ancestry tracing (2 products)
4. Case studies (initially 2)
5. Contact
(The headings are only indicative at this stage)
There is no pre-existing content yet. I'd like to work with lorem ipsum at the beginning. Some more imagery may have to be acquired, I am expecting that.
So far there is only a Facebook page https://www.examplebook.test/profile.php?id=48305716629384

Target Market(s)

Older people in Australia, more males than females

Industry/Entity Type

Personal services - Genealogy

Font styles to use
Serif
Decorative

Colors

Designer to choose colors to be used in the design.

Requirements
Must have
• Feel warm, feel trustworthy, clear call to action
Should not have
• Too small writing, confusing imagery

```html
<!DOCTYPE html>
<html lang="en">
<head>
<meta charset="utf-8">
<title>Martin J. Callow – Family History Specialist</title>
<link href="https://fonts.googleapis.com/css2?family=Cinzel:wght@400;500;600&family=Outfit:wght@400;500;600&display=swap" rel="stylesheet">
<style>
:root{
  --green:#0a6630;
  --green-dark:#07552a;
  --green-soft:#6fa97f;
  --cream:#f4eee3;
  --ink:#2e2e2e;
  --muted:#555;
  --white:#ffffff;
  --line:#e3e3e3;
}
*{box-sizing:border-box;margin:0;padding:0}
html,body{width:1200px;height:3660px;overflow:hidden;background:var(--white)}
body{font-family:"Outfit",Arial,sans-serif;color:var(--ink)}
.page{position:relative;width:1200px;height:3660px;overflow:hidden}
.abs{position:absolute}
h1,h2,h3,.serif{font-family:"Cinzel",Georgia,serif;font-weight:500;color:var(--green);letter-spacing:.5px}
.btn{position:absolute;display:flex;align-items:center;justify-content:center;border-radius:20px;background:var(--green);color:var(--white);font-weight:600;font-size:13px;text-decoration:none}
.btn--light{background:var(--cream);color:var(--green-dark)}

/* header */
.brand{left:94px;top:14px;display:flex;align-items:center;gap:12px}
.brand__mark{width:72px;height:72px;border-radius:50%;border:3px solid var(--green)}
.brand__name{font-family:"Cinzel",serif;font-size:20px;color:var(--green);line-height:1}
.brand__tag{font-family:"Cinzel",serif;font-size:10px;color:var(--green);margin-top:3px}
.topbar{right:94px;top:17px;display:flex;gap:22px;font-size:12px;color:var(--muted);align-items:center}
.topbar span{display:flex;align-items:center;gap:5px}
.flag-dot{width:14px;height:14px;border-radius:50%;background:#2c4b9a;display:inline-block}
.nav{left:561px;top:48px;width:501px;height:37px;border:1.5px solid var(--green);border-radius:20px;display:flex;align-items:center;justify-content:space-around;padding:0 4px 0 14px;font-size:13px;font-weight:600;color:var(--green-dark)}
.nav a{color:inherit;text-decoration:none;display:flex;align-items:center;gap:6px}
.nav .nav__cta{background:var(--green);color:var(--white);border-radius:16px;padding:8px 22px}
.cart{left:1068px;top:48px;width:38px;height:38px;border-radius:50%;background:var(--green);display:flex;align-items:center;justify-content:center}

/* circles */
.ring{position:absolute;border-radius:50%;border:9px solid var(--green);background:var(--white);padding:10px}
.ring .photo{width:100%;height:100%;border-radius:50%}

/* hero */
.hero__title{left:92px;top:258px;font-size:54px;line-height:54px;font-weight:500}
.hero__text{left:94px;top:428px;width:420px;font-size:17px;line-height:23px;color:var(--muted)}

/* about */
.about__title{left:635px;top:772px;font-size:34px;line-height:41px;width:470px}
.about__text{left:635px;top:902px;width:450px;font-size:14px;line-height:20px;color:var(--ink)}
.about__list{left:635px;top:1013px;font-size:14px;line-height:20px;list-style:none}

/* products */
.section-title{left:0;width:1200px;text-align:center;font-size:47px}
.tabs{top:1352px;font-family:"Cinzel",serif;font-size:20px;color:var(--green)}
.tab-underline{left:327px;top:1392px;width:104px;height:3px;background:var(--green)}
.pkg-adv{left:97px;top:1434px;width:461px;height:370px;background:var(--green);border-top-left-radius:72px}
.pkg-adv h3{position:absolute;left:52px;top:62px;color:var(--white);font-size:38px;line-height:40px}
.pkg-adv p{position:absolute;left:57px;top:156px;width:380px;color:var(--white);font-size:15px;line-height:21px}
.price{font-size:14px}
.price b{font-weight:400;font-size:26px}
.pkg-adv .price{position:absolute;left:57px;top:232px;color:var(--white)}
.family-photo{left:0;top:1804px;width:558px;height:374px;border-bottom-left-radius:80px;background:linear-gradient(135deg,#8a6e52,#c9b8a0 45%,#6b5d4c)}
.pkg-basic{left:561px;top:1560px;width:509px;height:618px;background:var(--cream);border-top-left-radius:60px;border-top-right-radius:250px;border-bottom-right-radius:150px}
.pkg-basic h3{position:absolute;left:81px;top:305px;font-size:38px;line-height:40px;color:var(--green-dark)}
.pkg-basic p{position:absolute;left:83px;top:395px;width:350px;font-size:14px;line-height:21px}
.pkg-basic .price{position:absolute;left:85px;top:464px}

/* banner */
.banner{left:94px;top:2280px;width:1011px;height:167px;border-radius:84px;background:linear-gradient(100deg,var(--green-dark),var(--green) 50%,var(--green-dark));text-align:center;color:var(--white)}
.banner h2{color:var(--white);font-size:34px;margin-top:48px}
.banner p{font-size:22px;margin-top:4px}
.banner a{color:var(--white)}

/* case study */
.case__title{left:648px;top:2678px;font-size:36px;line-height:38px;color:var(--green-dark)}
.case__text{left:648px;top:2764px;width:410px;font-size:14px;line-height:21px}
.badge{left:372px;top:2942px;width:170px;height:170px;border-radius:50%;background:var(--cream);display:flex;align-items:center;justify-content:center}
.badge span{width:134px;height:134px;border-radius:50%;border:3px solid var(--green);display:flex;align-items:center;justify-content:center;font-family:"Cinzel",serif;font-size:16px;color:var(--green);text-align:center;line-height:20px}
.arrow{width:34px;height:34px;border-radius:50%;display:flex;align-items:center;justify-content:center;top:2961px}

.divider{left:91px;top:3175px;width:1011px;height:1px;background:var(--line)}
.faq__title{left:94px;top:3240px;font-size:40px;color:var(--ink)}
.faq__text{left:94px;top:3291px;font-size:18px;color:var(--ink)}

/* footer */
.footer{left:0;top:3373px;width:1200px;height:300px;background:var(--green);border-top-left-radius:100px;border-top-right-radius:100px;color:var(--white)}
.footer .foot-brand{position:absolute;left:100px;top:70px;width:155px;text-align:center}
.foot-brand__mark{width:80px;height:80px;border-radius:50%;border:3px solid var(--white);margin:0 auto 10px}
.foot-brand__name{font-family:"Cinzel",serif;font-size:15px;line-height:16px}
.foot-brand__tag{font-family:"Cinzel",serif;font-size:8px}
.lang{position:absolute;left:324px;top:118px;width:149px;height:38px;border:1px solid rgba(255,255,255,.6);border-radius:20px;display:flex;align-items:center;padding:0 12px;gap:10px;font-size:13px}
.lang .flag-dot{width:24px;height:24px}
.foot-links{position:absolute;right:94px;top:103px;display:flex;gap:34px;font-size:13px;font-weight:600}
.foot-contact{position:absolute;right:94px;top:129px;font-size:13px;font-weight:600}
.foot-social{position:absolute;right:94px;top:157px;display:flex;gap:10px}
.foot-social span{width:11px;height:11px;border-radius:2px;background:var(--white)}
.foot-rule{position:absolute;left:94px;top:231px;width:1012px;height:1px;background:rgba(255,255,255,.35)}
.copy{position:absolute;left:94px;top:251px;font-size:13px}
.cards{position:absolute;left:994px;top:248px;display:flex;gap:10px}
.cards span{width:34px;height:22px;border-radius:5px;background:var(--white)}
.cards span:nth-child(2){background:#e9e9e9}
.to-top{position:absolute;left:1139px;top:221px;width:34px;height:34px;border-radius:50%;background:#dfe7e1;display:flex;align-items:center;justify-content:center}
</style>
</head>
<body>
<div class="page">

  <!-- header -->
  <div class="abs brand">
    <div class="brand__mark"></div>
    <div>
      <div class="brand__name">MARTIN J. CALLOW</div>
      <div class="brand__tag">FAMILY HISTORY SPECIALIST</div>
    </div>
  </div>
  <div class="abs topbar">
    <span><svg width="11" height="11" viewBox="0 0 24 24"><path fill="#0a6630" d="M6.6 10.8a15 15 0 0 0 6.6 6.6l2.2-2.2c.3-.3.7-.4 1-.2 1.1.4 2.3.6 3.6.6.6 0 1 .4 1 1V20c0 .6-.4 1-1 1A17 17 0 0 1 3 4c0-.6.4-1 1-1h3.5c.6 0 1 .4 1 1 0 1.3.2 2.5.6 3.6.1.3 0 .7-.2 1z"/></svg>+61 XXXXXXXXX</span>
    <span><svg width="12" height="10" viewBox="0 0 24 18"><rect x="1" y="1" width="22" height="16" rx="2" fill="#0a6630"/><path d="M2 2l10 8 10-8" stroke="#fff" stroke-width="2" fill="none"/></svg>info@martincallow.test</span>
    <span><i class="flag-dot"></i>En ⌄</span>
  </div>
  <nav class="abs nav">
    <a href="#">
      <svg width="13" height="12" viewBox="0 0 24 22"><path fill="#0a6630" d="M12 1 1 11h3v10h6v-6h4v6h6V11h3z"/></svg>Home</a>
    <a href="#">About Us</a>
    <a href="#">Services</a>
    <a href="#">Case Studies</a>
    <a href="#" class="nav__cta">Contact</a>
  </nav>
  <div class="abs cart">
    <svg width="16" height="15" viewBox="0 0 24 22"><path d="M1 2h4l3 12h12l3-9H7" stroke="#fff" stroke-width="2" fill="none"/><circle cx="10" cy="19" r="2" fill="#fff"/><circle cx="18" cy="19" r="2" fill="#fff"/></svg>
  </div>

  <!-- hero -->
  <h1 class="abs hero__title">UNLOCK THE<br>PAST,DISCOVER<br>YOUR LEGACY</h1>
  <p class="abs hero__text">Trace your roots, uncover lost stories, and connect with your heritage.</p>
  <a class="btn" href="#" style="left:94px;top:490px;width:165px;height:33px">Start Your Journey</a>
  <div class="ring" style="left:539px;top:116px;width:566px;height:566px">
    <div class="photo" role="img" aria-label="Child sitting high on a moss-covered tree in a green forest" style="background:radial-gradient(circle at 50% 35%,#9fb76a,#4f6b2a 55%,#2c3e18)"></div>
  </div>

  <!-- about -->
  <div class="ring" style="left:95px;top:684px;width:506px;height:506px">
    <div class="photo" role="img" aria-label="Silhouette of a family walking beneath a glowing tree intertwined with a golden DNA helix" style="background:radial-gradient(circle at 30% 40%,#f4dfa0,#a78a55 35%,#3b3a36 70%,#1f2529)"></div>
  </div>
  <h2 class="abs about__title">MEET MARTIN J. CALLOW – YOUR FAMILY HISTORY SPECIALIST</h2>
  <p class="abs about__text">Martin J. Callow is passionate about uncovering family stories. With years of experience in genealogy research, he has helped hundreds of families reconnect with their heritage. Whether through traditional records or cutting-edge DNA analysis, every family has a unique history waiting to be discovered.</p>
  <ul class="abs about__list">
    <li>Expert in historical records research</li>
    <li>Specialist in DNA ancestry tracing</li>
    <li>Helping Australians connect with their past</li>
  </ul>
  <a class="btn" href="#" style="left:635px;top:1089px;width:121px;height:33px">Learn More</a>

  <!-- products -->
  <h2 class="abs section-title" style="top:1270px">PRODUCTS &amp; SERVICES</h2>
  <div class="abs tabs" style="left:192px">TRADITIONAL GENEALOGY RESEARCH</div>
  <div class="abs tabs" style="left:668px;color:var(--ink)">DNA-BASED ANCESTRY TRACING</div>
  <div class="abs tab-underline"></div>

  <div class="abs pkg-basic">
    <h3>BASIC FAMILY<br>TREE PACKAGE</h3>
    <p>We research and provide a 3-generation family tree based on available records. (Delivery: Digital report &amp; family chart)</p>
    <div class="price">Price: <b>AUD 199</b></div>
    <a class="btn" href="#" style="left:81px;top:517px;width:119px;height:34px">Add to Cart</a>
  </div>
  <div class="ring" style="left:623px;top:1428px;width:384px;height:384px;padding:8px">
    <div class="photo" role="img" aria-label="Hands holding old family photographs and letters in front of a laptop" style="background:radial-gradient(circle at 50% 45%,#b9aa94,#6b5c4c 60%,#3a302a)"></div>
  </div>
  <div class="abs pkg-adv">
    <h3>ADVANCED FAMILY<br>HISTORY PACKAGE</h3>
    <p>Full research covering up to 6 generations, including detailed reports, documents, and historical narratives. (Delivery: Digital + optional printed book)</p>
    <div class="price">Price: <b>AUD 499</b></div>
    <a class="btn btn--light" href="#" style="left:52px;top:281px;width:120px;height:34px">Add to Cart</a>
  </div>
  <div class="abs family-photo" role="img" aria-label="Family of four looking through photo albums together at a table"></div>

  <!-- banner -->
  <div class="abs banner">
    <h2>NEED A CUSTOM RESEARCH PLAN?</h2>
    <p><a href="#">Contact us</a> for a personalized package!</p>
  </div>

  <!-- case studies -->
  <h2 class="abs section-title" style="top:2520px">CASE STUDIES</h2>
  <div class="ring" style="left:132px;top:2596px;width:468px;height:468px">
    <div class="photo" role="img" aria-label="Smiling multi-generation family standing together in a park" style="background:radial-gradient(circle at 50% 40%,#c9c0a8,#7d8a5e 55%,#3f4a2f)"></div>
  </div>
  <div class="abs badge"><span>M.J.<br>CALLOW</span></div>
  <h2 class="abs case__title">JOHN’S LOST FAMILY<br>FOUND THROUGH DNA</h2>
  <p class="abs case__text">John had always wondered about his grandfather, a man he had only heard stories about but never met. With no official records to trace his lineage, he turned to our DNA-based ancestry service. Through genetic matching and historical records, we uncovered a network of relatives in Ireland, reconnecting John with long-lost family members. The journey not only provided him with answers but also led to an emotional reunion that reshaped his understanding of his roots.</p>
  <a class="btn" href="#" style="left:648px;top:2961px;width:121px;height:34px">Read More</a>
  <div class="abs arrow" style="left:970px;background:var(--cream);color:var(--green)">‹</div>
  <div class="abs arrow" style="left:1008px;background:var(--green-soft);color:var(--white)">›</div>

  <div class="abs divider"></div>
  <h2 class="abs faq__title">HAVE QUESTIONS?</h2>
  <p class="abs faq__text">Have questions? Ready to start your family research journey? Get in touch today!</p>
  <a class="btn" href="#" style="left:956px;top:3259px;width:147px;height:43px;border-radius:22px;font-size:16px">Contact Us</a>

  <!-- footer -->
  <footer class="abs footer">
    <div class="foot-brand">
      <div class="foot-brand__mark"></div>
      <div class="foot-brand__name">MARTIN J. CALLOW</div>
      <div class="foot-brand__tag">FAMILY HISTORY SPECIALIST</div>
    </div>
    <div class="lang"><i class="flag-dot"></i>English<span style="margin-left:auto">⌄</span></div>
    <div class="foot-links"><span>Home</span><span>About Us</span><span>Services</span><span>Case Studies</span><span>Contact Us</span></div>
    <div class="foot-contact">Australia | contact@callowhistory.test | +61 X XXXX XXXX</div>
    <div class="foot-social"><span></span><span></span><span></span><span></span></div>
    <div class="foot-rule"></div>
    <div class="copy">Copyright © 2024 Martin J. Callow Family History Specialist. All rights reserved.</div>
    <div class="cards"><span></span><span></span><span></span></div>
    <div class="to-top"><svg width="10" height="6" viewBox="0 0 10 6"><path d="M1 5l4-4 4 4" stroke="#0a6630" stroke-width="1.5" fill="none"/></svg></div>
  </footer>
</div>
</body>
</html>
```